M25 Billboard Advert Required Please

I need an advert for a motorway Billboard on the M25 , the advert should show the following in big letters:
GUTTER CLEANING
DALRYNFLUES.COM and a small logo off to the side (Our logo is attached)

The printer has requested the following (Important please) the advert has to be
pdf file / 300 dpi/landscape orientation / scaled to a minimum 25% advert size ( this particular site is 22ft x 10ft so 25% of this please). Please also make sure that the artwork is embedded and outlined correctly if this is incorrect it will affect the printing of the banner.

Target Market(s)

General Public

Industry/Entity Type

Gutter Cleaning

Requirements
Should not have
• No Change to our Logo

```html
<!DOCTYPE html>
<html lang="en">
<head>
<meta charset="utf-8">
<title>Dalryn Flues – Gutter Cleaning Billboard</title>
<link href="https://fonts.googleapis.com/css2?family=Anton&family=Open+Sans:wght@600;700&family=Oswald:wght@700&display=swap" rel="stylesheet">
<style>
  :root {
    --backdrop: #d9d9d9;
    --paper: #ffffff;
    --ink: #141414;
    --brand-red: #b50f20;
  }
  * { margin: 0; padding: 0; box-sizing: border-box; }
  html, body {
    width: 1000px;
    height: 1200px;
    overflow: hidden;
    background: var(--backdrop);
  }
  .billboard {
    position: absolute;
    left: 40px;
    top: 370px;
    width: 920px;
    height: 460px;
    background: var(--paper);
    box-shadow: 0 10px 40px rgba(0,0,0,0.25);
    overflow: hidden;
  }
  .brand-area {
    height: 183px;
    display: flex;
    flex-direction: column;
    align-items: center;
    justify-content: center;
    gap: 18px;
    padding-top: 12px;
  }
  .brand {
    display: flex;
    align-items: center;
    gap: 16px;
  }
  .brand-mark {
    width: 34px;
    height: 34px;
    background: var(--brand-red);
  }
  .brand-name {
    font-family: "Open Sans", sans-serif;
    font-weight: 700;
    font-size: 46px;
    line-height: 1;
    color: var(--ink);
  }
  .tagline {
    font-family: "Open Sans", sans-serif;
    font-weight: 600;
    font-size: 21px;
    color: var(--ink);
  }
  .divider {
    height: 11px;
    background: var(--ink);
  }
  .service-band {
    height: 151px;
    background: var(--brand-red);
  }
  .url-band {
    height: 115px;
    background: var(--ink);
  }
  .service-band svg, .url-band svg {
    display: block;
    width: 100%;
    height: 100%;
  }
  .headline {
    font-family: "Anton", sans-serif;
    font-size: 118px;
    fill: var(--paper);
    stroke: var(--ink);
    stroke-width: 7px;
    stroke-linejoin: round;
    paint-order: stroke fill;
  }
  .web-address {
    font-family: "Oswald", sans-serif;
    font-weight: 700;
    font-size: 86px;
    fill: var(--paper);
  }
</style>
</head>
<body>
  <main class="billboard">
    <header class="brand-area">
      <div class="brand">
        <span class="brand-mark"></span>
        <span class="brand-name">Dalryn Flues</span>
      </div>
      <p class="tagline">Clean gutters protect your property</p>
    </header>
    <div class="divider"></div>
    <section class="service-band">
      <svg viewBox="0 0 920 151" aria-label="Gutter Cleaning">
        <text class="headline" x="460" y="126" text-anchor="middle" textLength="850" lengthAdjust="spacingAndGlyphs">GUTTER CLEANING</text>
      </svg>
    </section>
    <section class="url-band">
      <svg viewBox="0 0 920 115" aria-label="dalrynflues.com">
        <text class="web-address" x="460" y="95" text-anchor="middle" textLength="720" lengthAdjust="spacingAndGlyphs">DALRYNFLUES.COM</text>
      </svg>
    </section>
  </main>
</body>
</html>
```